Business Card Design Project

I have attached the logo and the colour pallete for the branding for the company.

Creative designs for business cards are needed.

The Company is modern corporate.

Industry/Entity Type

Business

```html
<!DOCTYPE html>
<html lang="en">
<head>
<meta charset="utf-8">
<title>Northway Business Card</title>
<link href="https://fonts.googleapis.com/css2?family=Montserrat:wght@400;500;600;700&display=swap" rel="stylesheet">
<style>
  :root {
    --purple-deep: #3e1742;
    --purple: #5a1f5a;
    --purple-light: #6e2a6c;
    --ink-purple: #5b1f5c;
    --orange: #e8761e;
    --card-white: #ececec;
    --stage: #d9d6d2;
    --white: #ffffff;
  }
  * { box-sizing: border-box; margin: 0; padding: 0; }
  html, body {
    width: 1200px; height: 900px; overflow: hidden;
    background: var(--stage);
    font-family: "Montserrat", sans-serif;
  }
  .stage {
    width: 1200px; height: 900px;
    display: flex; align-items: center; justify-content: center; gap: 60px;
  }
  .card {
    width: 525px; height: 300px; position: relative; overflow: hidden;
    box-shadow: 0 6px 18px rgba(0,0,0,0.18);
  }
  /* Front */
  .card-front {
    background: radial-gradient(ellipse at 35% 30%, var(--purple-light) 0%, var(--purple) 45%, var(--purple-deep) 100%);
    color: var(--white);
    display: flex; flex-direction: column; align-items: center; justify-content: center;
  }
  .brand-name {
    font-weight: 600; font-size: 68px; letter-spacing: -1px; line-height: 1;
  }
  .front-rule {
    width: 300px; border-top: 2px dotted rgba(255,255,255,0.6); margin: 24px 0 18px;
  }
  .front-url { font-weight: 400; font-size: 18px; letter-spacing: 0.5px; }
  /* Back */
  .card-back { background: var(--card-white); color: var(--ink-purple); }
  .pointer { position: absolute; left: 0; top: 50px; }
  .details { position: absolute; left: 128px; top: 58px; width: 215px; white-space: nowrap; }
  .person-name { font-weight: 700; font-size: 16px; letter-spacing: 0.3px; text-transform: uppercase; line-height: 1.2; }
  .person-role { font-weight: 400; font-size: 13px; margin-top: 2px; }
  .details-rule { border-top: 2px dotted var(--ink-purple); margin: 12px 0 12px; opacity: 0.7; }
  .contact-list { list-style: none; font-size: 12.5px; line-height: 1.45; }
  .contact-list span { display: inline-block; width: 22px; }
  .address { font-size: 12.5px; line-height: 1.45; margin-top: 12px; }
  .back-url { color: var(--orange); font-size: 13px; margin-top: 16px; }
  .back-brand {
    position: absolute; right: 30px; top: 108px;
    font-weight: 600; font-size: 34px; letter-spacing: -0.5px; line-height: 1;
    color: var(--ink-purple); white-space: nowrap;
  }
</style>
</head>
<body>
<main class="stage">
  <section class="card card-front">
    <div class="brand-name">northway</div>
    <div class="front-rule"></div>
    <div class="front-url">www.northwayhub.com</div>
  </section>

  <section class="card card-back">
    <svg class="pointer" width="124" height="40" viewBox="0 0 124 40" aria-hidden="true">
      <path d="M0 6 Q55 10 104 22" fill="none" stroke="var(--ink-purple)" stroke-width="3"/>
      <polygon points="96,12 118,25 94,31" fill="var(--ink-purple)"/>
    </svg>
    <div class="details">
      <div class="person-name">Daniel Reyes Moore</div>
      <div class="person-role">Founder &amp; CEO</div>
      <div class="details-rule"></div>
      <ul class="contact-list">
        <li><span>T</span>555 204 7188</li>
        <li><span>M</span>555 204 7188</li>
        <li><span>E</span>daniel@northwayhub.com</li>
      </ul>
      <div class="address">Calle Olmo 14, Col. Verde<br>City DF 04120, MX.</div>
      <div class="back-url">www.northwayhub.com</div>
    </div>
    <div class="back-brand">northway</div>
  </section>
</main>
</body>
</html>
```